Redesign Current Website Into An Exciting Updated Design

We need to redesign the current website www.gleamvoucherhub.com We want an overall new look. We are rebranding so it will be a new logo and we would like to see new images as well so you cannot compare the old from the new.

You can use same exact content as on current url www.gleamvoucherhub.com

The website must be warm and inviting and fun yet professional and modern.

The website must also be designed with mobile in mind

The website must be warm and inviting yet professional and modern.

The website must also be designed with mobile in mind.

Target Market(s)

Consumers redeeming rewards

Industry/Entity Type

Promotional Reward Fullfillment

Coding

Coded - Design and coding required

Number of Pages Required

3 page

Requirements
Must have
• This website is a website where consumers come to redeem rewards they received from doing business with a company that offers these rewards. So the website should be very inviting.
Nice to have
• open
Should not have
• open

```html
<!DOCTYPE html>
<html lang="en">
<head>
<meta charset="utf-8">
<title>Gleam Voucher Hub – Redeem Your Rewards</title>
<link href="https://fonts.googleapis.com/css2?family=Bebas+Neue&family=Inter:wght@400;500;600;700&display=swap" rel="stylesheet">
<style>
:root{
  --navy:#0a4a87;
  --blue:#1d5f9c;
  --sky:#e3f0fb;
  --pale:#f3f4f6;
  --accent:#2d9bf0;
  --ink:#1b1b1b;
  --white:#ffffff;
  --line:#d7dde4;
}
*{box-sizing:border-box;margin:0;padding:0}
html,body{width:1200px;height:3431px;overflow:hidden}
body{font-family:"Inter",Arial,sans-serif;color:var(--ink);position:relative;background:var(--white)}
.display{font-family:"Bebas Neue",Impact,sans-serif;letter-spacing:1px;font-weight:400}
section,header,footer{position:absolute;left:0;width:1200px}
.abs{position:absolute}
.center{text-align:center;left:0;width:1200px}
.btn{position:absolute;display:flex;align-items:center;justify-content:center;font-family:"Bebas Neue",Impact,sans-serif;font-size:17px;letter-spacing:1px;color:var(--white);background:var(--navy);border:2px solid var(--accent)}

/* hero */
.hero{top:0;height:637px;background:linear-gradient(180deg,#2f6ea6 0%,#4a88bd 30%,#3a8fa8 55%,#d9c2a0 85%,#c6a985 100%)}
.brand{position:absolute;left:150px;top:46px;color:var(--white);font-family:"Bebas Neue",sans-serif;font-size:20px;line-height:18px;display:flex;align-items:center;gap:8px}
.brand .mark{width:16px;height:16px;border:2px solid var(--white)}
.nav{position:absolute;right:152px;top:62px;display:flex;gap:22px;font-family:"Bebas Neue",sans-serif;font-size:17px;letter-spacing:1px;color:var(--white)}
.nav .active{color:var(--accent)}
.hero h1{position:absolute;top:140px;font-size:46px;color:var(--white);letter-spacing:3px}
.hero p{position:absolute;top:200px;font-size:13.5px;line-height:20px;color:var(--white)}
.field{position:absolute;top:290px;height:31px;border:2px solid #9fc3e2;background:rgba(255,255,255,.08);color:#e8f1f9;font-size:11px;padding:7px 10px}

/* steps */
.steps{top:637px;height:429px;background:linear-gradient(180deg,var(--pale) 0%,var(--sky) 100%)}
.h2{position:absolute;font-family:"Bebas Neue",sans-serif;font-size:30px;letter-spacing:1px;color:var(--navy)}
.lead{position:absolute;font-size:13.5px;line-height:20px;color:#222}
.dot{position:absolute;width:46px;height:46px;border-radius:50%;background:var(--navy);border:3px solid #5aa6e6;color:var(--white);font-weight:700;font-size:17px;display:flex;align-items:center;justify-content:center}
.step-label{position:absolute;width:240px;text-align:center;font-size:11.5px;font-weight:600;line-height:16px}

/* rewards */
.rewards{top:1066px;height:566px;background:var(--navy);color:var(--white)}
.rewards .h2{color:var(--white)}
.rewards .lead{color:var(--white)}
.reward{position:absolute;top:178px;width:204px;text-align:center}
.reward .pic{width:152px;height:152px;border-radius:50%;border:3px solid #4fa3ea;margin:0 auto}
.reward h3{font-size:13.5px;font-weight:600;margin-top:16px}
.reward h4{font-size:11.5px;font-weight:700;margin-top:8px}
.reward p{font-size:10px;line-height:16px;margin-top:2px}

/* about */
.about{top:1632px;height:554px;background:var(--white)}
.process{position:absolute;left:150px;top:238px;width:456px;font-size:13px;line-height:20px;color:#222}
.process h3{font-family:"Bebas Neue",sans-serif;font-size:20px;font-weight:400;letter-spacing:.5px;margin-bottom:14px;color:#111}
.process p{margin-bottom:19px}
.process b{color:var(--blue);font-weight:600}
.circle-pic{position:absolute;border-radius:50%}

/* testimonials */
.reviews{top:2186px;height:381px;background:var(--sky)}
.card{position:absolute;top:164px;width:283px;height:152px;background:var(--navy);border-radius:12px;color:var(--white);padding:20px 20px}
.card p{font-size:9.6px;line-height:16px}
.card .who{position:absolute;left:22px;bottom:22px;font-size:9.5px}
.card .who b{font-weight:700}
.card .stars{position:absolute;right:22px;bottom:20px;display:flex;gap:3px}

/* partners */
.partners{top:2567px;height:364px;background:var(--white)}
.logo-box{position:absolute;top:173px;width:169px;height:71px;border:1px solid var(--line);display:flex;align-items:center;justify-content:center;gap:7px;font-weight:700;font-size:15px;color:var(--navy)}
.logo-box i{width:12px;height:12px;background:var(--navy);display:block}

/* help */
.help{top:2931px;height:150px;background:var(--sky)}

/* footer */
.footer{top:3081px;height:289px;background:var(--navy);border-radius:90px 90px 0 0;color:var(--white)}
.footer .col-title{position:absolute;top:58px;font-family:"Bebas Neue",sans-serif;font-size:16px;letter-spacing:1px;border-bottom:1px solid #6e9cc8;padding-bottom:2px}
.footer ul{position:absolute;list-style:none;font-size:11.5px;line-height:23.3px}
.footer .addr{position:absolute;left:150px;top:120px;font-size:10.5px;line-height:20px}
.footer .contact{position:absolute;left:150px;font-size:11.5px;display:flex;align-items:center;gap:8px}
.bottom{top:3370px;height:61px;background:var(--sky);font-size:10px;color:var(--navy)}
</style>
</head>
<body>

<header class="hero">
  <div class="abs" role="img" aria-label="Photo of a woman in a sun hat relaxing on striped beach chairs by a tropical lagoon" style="inset:0"></div>
  <div class="brand"><span class="mark"></span><span>GLEAM VOUCHER<br>HUB</span></div>
  <nav class="nav"><span class="active">HOME</span><span>ABOUT</span><span>HOW IT WORKS</span><span>FAQS</span><span>CONTACT</span></nav>
  <h1 class="display center">UNLOCK YOUR REWARDS – REDEEM &amp; ENJOY!</h1>
  <p class="center">Enter your certificate number and email to access your exclusive rewards.<br>Discover amazing travel vouchers, dining incentives, digital products, and more.<br>Redeeming your reward is quick and hassle-free!</p>
  <div class="field" style="left:322px;width:187px">Certificate Number</div>
  <div class="field" style="left:529px;width:188px">Email Address</div>
  <div class="btn" style="left:737px;top:290px;width:113px;height:31px;font-size:14px">REDEEM NOW</div>
</header>

<section class="steps">
  <div class="abs" role="img" aria-label="Faint gift box outline decoration" style="left:968px;top:70px;width:232px;height:260px;border:10px solid rgba(10,74,135,.05);border-radius:30px"></div>
  <h2 class="h2 center" style="top:60px">REDEEM YOUR REWARDS IN 3 EASY STEPS!</h2>
  <p class="lead center" style="top:103px">Unlock your rewards with our simple and hassle-free process. Just follow these three<br>easy steps and start enjoying your exclusive benefits!</p>
  <svg class="abs" style="left:0;top:0" width="1200" height="429">
    <path d="M388 209 C470 200 545 220 580 280" fill="none" stroke="#5aa6e6" stroke-width="1.5" stroke-dasharray="4 4"/>
    <path d="M620 280 C650 230 700 210 775 210" fill="none" stroke="#5aa6e6" stroke-width="1.5" stroke-dasharray="4 4"/>
    <path d="M574 274 l6 6 l1-8" fill="none" stroke="#5aa6e6" stroke-width="1.5"/>
    <path d="M768 205 l7 5 l-7 4" fill="none" stroke="#5aa6e6" stroke-width="1.5"/>
  </svg>
  <div class="dot" style="left:339px;top:188px">1</div>
  <div class="dot" style="left:583px;top:276px">2</div>
  <div class="dot" style="left:782px;top:188px">3</div>
  <div class="step-label" style="left:240px;top:245px">Enter your<br>certificate number and email</div>
  <div class="step-label" style="left:483px;top:333px">Select your<br>reward and follow the instructions</div>
  <div class="step-label" style="left:687px;top:245px">Redeem<br>and enjoy!</div>
</section>

<section class="rewards">
  <h2 class="h2 center" style="top:42px">EXPLORE YOUR EXCLUSIVE REWARDS!</h2>
  <p class="lead center" style="top:87px">Unlock amazing rewards designed to enhance your lifestyle. Choose from travel vouchers,<br>dining incentives, digital products, and more. Redeeming your reward is simple—just select a<br>category and follow the steps!</p>
  <div class="reward" style="left:65px"><div class="pic" role="img" aria-label="Aerial photo of a tropical resort pool" style="background:radial-gradient(circle,#39b7c7,#c9b48e)"></div><h3>VACATION CERTIFICATES</h3><h4>Enjoy a dream getaway!</h4><p>Redeem your vacation certificate for exclusive hotel stays, tropical resorts, and relaxing destinations.</p></div>
  <div class="reward" style="left:282px"><div class="pic" role="img" aria-label="Photo of passports, tickets and a toy plane" style="background:linear-gradient(135deg,#3fa1e0,#f5c23a)"></div><h3>TRAVEL VOUCHERS</h3><h4>Fly to your next adventure!</h4><p>Use travel vouchers to book discounted flights, hotel accommodations, and exciting travel experiences.</p></div>
  <div class="reward" style="left:493px"><div class="pic" role="img" aria-label="Photo of a keyboard, phone and mouse on colourful paper" style="background:linear-gradient(135deg,#f07b22,#e0d23f)"></div><h3>DIGITAL PRODUCTS</h3><h4>Upgrade your tech game!</h4><p>Choose from a selection of digital prod-ucts, including smart gadgets, head-phones, and e-gift cards.</p></div>
  <div class="reward" style="left:708px"><div class="pic" role="img" aria-label="Photo of a plated dinner with red wine" style="background:radial-gradient(circle,#e8e8e8,#2a3b2a)"></div><h3>DINING INCENTIVES</h3><h4>Dine out and indulge!</h4><p>Get discounts at top restaurants and enjoy delicious meals with family and friends.</p></div>
  <div class="reward" style="left:922px"><div class="pic" role="img" aria-label="Photo of a shopping cart full of fresh produce" style="background:radial-gradient(circle,#e4b53a,#2d6e3a)"></div><h3>GAS &amp; GROCERY REWARDS</h3><h4>Save on essentials!</h4><p>Redeem your reward for gas savings or grocery discounts to cut down on every-day expenses.</p></div>
  <div class="btn" style="left:477px;top:476px;width:237px;height:43px;gap:10px">REDEEM YOUR OFFER NOW
    <svg width="18" height="18" viewBox="0 0 18 18" fill="none" stroke="#fff" stroke-width="1.3"><rect x="2" y="7" width="14" height="9"/><rect x="1" y="4" width="16" height="3"/><path d="M9 4v12M9 4C7 1 4 1 5 4M9 4c2-3 5-3 4 0"/></svg>
  </div>
</section>

<section class="about">
  <div class="abs" role="img" aria-label="Faint gift box outline decoration" style="left:0;top:140px;width:210px;height:300px;border:10px solid rgba(10,74,135,.05);border-left:none"></div>
  <h2 class="h2 center" style="top:58px">WHO WE ARE &amp; WHAT WE DO</h2>
  <p class="lead center" style="top:105px">At Gleam Voucher Hub, we specialize in providing marketing incentives that help businesses<br>attract and retain customers. We manage the redemption and fulfillment process for a variety of<br>exciting rewards—including vacation certificates, travel vouchers, digital products,<br>dining incentives, and gas &amp; grocery rewards.</p>
  <div class="process">
    <h3>REDEMPTION &amp; FULFILLMENT PROCESS</h3>
    <p><b>Step 1:</b> Businesses offer rewards to their customers through promotions, giveaways, or loyalty programs.</p>
    <p><b>Step 2:</b> Customers receive a certificate or voucher and enter their details on our easy-to-use platform.</p>
    <p><b>Step 3:</b> Our team verifies the information and processes the redemption.</p>
    <p><b>Step 4:</b> Customers receive their rewards, while businesses enjoy increased engagement and brand loyalty.</p>
  </div>
  <div class="circle-pic" role="img" aria-label="Photo of friends on a boat among tropical islands" style="left:641px;top:221px;width:178px;height:178px;background:linear-gradient(180deg,#4aa3d8,#8a7a66)"></div>
  <div class="circle-pic" role="img" aria-label="Photo of hands typing on a laptop on a pink desk" style="left:870px;top:221px;width:178px;height:178px;background:linear-gradient(135deg,#f6b6c6,#e78aa4)"></div>
  <div class="circle-pic" role="img" aria-label="Photo of a passenger jet in a blue sky" style="left:758px;top:318px;width:178px;height:178px;background:linear-gradient(180deg,#3d8fd6,#cfe4f5)"></div>
</section>

<section class="reviews">
  <div class="abs" role="img" aria-label="Faint world map background" style="inset:0;background:radial-gradient(ellipse at 50% 50%,rgba(10,74,135,.05),transparent 70%)"></div>
  <h2 class="h2 center" style="top:45px">WHAT OUR HAPPY CUSTOMERS SAY</h2>
  <p class="lead center" style="top:92px">We've helped thousands of customers redeem their rewards smoothly and hassle-free.<br>See what they have to say about their experience!</p>
  <div class="card" style="left:150px"><p>Wonderful! It was just like being in Rome, but only with great shows to enjoy. The rooms of the hotel and service were excellent. Going through the travel agency was simple and easy on the purse strings.</p><div class="who"><b>Marcus T.</b> Flagstaff, AZ</div><div class="stars">★★★★★</div></div>
  <div class="card" style="left:459px"><p>Very good. Las Vegas was a dream trip. Would go again without a doubt. It's the best. The hotels, the streets, the Grand Canyon. Everything is very good!</p><div class="who"><b>Lena P.</b> Orlando, FL</div><div class="stars">★★★★★</div></div>
  <div class="card" style="left:766px"><p style="font-size:9px;line-height:16px">It was GREAT! I've always wanted to go to Vegas. Being able to stay right on the strip was great. I love that we were able to walk to a lot of the sites. The fountains at the Grand Azure were AMAZING! I LOVED the atmosphere and the food. The whole experience was awesome. I would love to return.</p><div class="who"><b>Marcus T.</b> Flagstaff, AZ</div><div class="stars">★★★★★</div></div>
</section>

<section class="partners">
  <h2 class="h2 center" style="top:62px">TRUSTED BY LEADING BRANDS WORLDWIDE</h2>
  <p class="lead center" style="top:109px">We're proud to work with businesses of all sizes, helping them enhance their marketing efforts with<br>exciting rewards and incentives. Here are just a few of the brands that trust us!</p>
  <div class="logo-box" style="left:150px"><i></i>Northgate Homes</div>
  <div class="logo-box" style="left:332px">Cartwell</div>
  <div class="logo-box" style="left:515px"><i></i>Veloxa Motors</div>
  <div class="logo-box" style="left:697px">Skyrise TV</div>
  <div class="logo-box" style="left:879px"><i></i>Oakfield Cover</div>
  <div class="btn" style="left:509px;top:276px;width:197px;height:41px;font-size:15px">WANT TO PARTNER WITH US?</div>
</section>

<section class="help">
  <h2 class="h2" style="left:150px;top:40px;font-size:28px">NEED HELP? GET IN TOUCH!</h2>
  <p class="lead" style="left:150px;top:84px;font-size:13px">We're here to assist you! Whether you have questions about redeeming your<br>rewards or need support, our team is ready to help.</p>
  <div class="btn" style="left:850px;top:57px;width:198px;height:42px;font-size:16px">LOGIN TO YOUR ACCOUNT</div>
</section>

<footer class="footer">
  <div class="brand" style="top:58px"><span class="mark"></span><span>GLEAM VOUCHER<br>HUB</span></div>
  <div class="addr">88 Harbor Lane, Suite 210,<br>Lakeside,<br>CA 90210, USA</div>
  <div class="contact" style="top:193px"><svg width="14" height="14" viewBox="0 0 14 14" fill="none" stroke="#fff" stroke-width="1.1"><path d="M3 1l2 3-1 1.5c1 2 2.5 3.5 4.5 4.5L10 9l3 2-1 2C6 13 1 8 1 2z"/></svg>+1 (555) 010-2288</div>
  <div class="contact" style="top:221px"><svg width="14" height="12" viewBox="0 0 14 12" fill="none" stroke="#fff" stroke-width="1.1"><rect x="1" y="1" width="12" height="10"/><path d="M1 1l6 5 6-5"/></svg>support@gleamvoucherhub.com</div>
  <div class="col-title" style="left:512px">QUICK LINKS</div>
  <ul style="left:514px;top:100px"><li>Home</li><li>About Us</li><li>How It Works</li><li>Available Rewards</li><li>Testimonials</li><li>Contact &amp; Support</li><li>FAQ</li></ul>
  <div class="col-title" style="left:797px">BUSINESS HOURS</div>
  <ul style="left:799px;top:100px;font-size:10.5px;line-height:22px">
    <li>◷&nbsp;&nbsp; Monday – Friday: 9:00 AM – 6:00 PM (EST)</li>
    <li>◷&nbsp;&nbsp; Saturday &amp; Sunday: Closed</li>
  </ul>
</footer>

<section class="bottom">
  <div class="abs" style="left:150px;top:26px">© Copyright 2005-2025. All Rights Reserved.</div>
  <div class="abs" style="right:152px;top:26px;display:flex;gap:17px"><span>Privacy Policy</span><span>Terms Of Use</span></div>
</section>

</body>
</html>
```